Bellcrest HVAC Business Card design

Looking for a modern professional two sided design. Showing contact info and services provided. Possibly on a silk card stock.
Using blues or greens or greys and maybe metallic. One color or a mixture of these.
Dorian Vance
dvance@bellcresthvac-example.net
555-318-4702
Air Conditioning
Heating
Heat Pumps / Gas / Oil
Ductless mini splits
Controls
VFD's
Pumps
Gas Fitting/Piping
Service and New install
Residential / Commercial
Industry/Entity Type
Mechanical HVAC
Contact Information for Business Card
Logo, contact info and provided services

```html
<!DOCTYPE html>
<html lang="en">
<head>
<meta charset="utf-8">
<title>Bellcrest HVAC Business Card</title>
<link href="https://fonts.googleapis.com/css2?family=Montserrat:wght@400;500;700&display=swap" rel="stylesheet">
<style>
  :root {
    --teal-deep: #1f8068;
    --teal-light: #52dcaa;
    --teal-text: #1e7d66;
    --orange: #f9a825;
    --white: #ffffff;
    --ink: #333a3f;
    --ink-soft: #3f474c;
    --page: #e3e8ea;
    --air: #8ee21f;
    --cool: #7ff0d7;
    --water: #0c1f6e;
    --fire: #f2511b;
  }
  * { box-sizing: border-box; margin: 0; padding: 0; }
  html, body { width: 1200px; height: 1200px; overflow: hidden; }
  body {
    background: var(--page);
    font-family: "Montserrat", sans-serif;
    position: relative;
  }
  .card {
    position: absolute;
    left: 120px;
    width: 960px;
    height: 548px;
    overflow: hidden;
    background: var(--white);
  }
  .card-front { top: 32px; }
  .card-back { top: 620px; }
  .card-bg { position: absolute; inset: 0; width: 100%; height: 100%; }

  .brand {
    position: absolute;
    left: 0; right: 0;
    top: 148px;
    text-align: center;
    color: var(--white);
    font-weight: 700;
    line-height: 1;
  }
  .brand-name { display: block; font-size: 66px; letter-spacing: 2px; }
  .brand-trade { display: block; font-size: 44px; letter-spacing: 6px; margin-top: 10px; }

  .illustration-slot {
    position: absolute;
    left: 40px; top: 36px;
    width: 330px; height: 512px;
    border-radius: 150px 150px 0 0;
    background: linear-gradient(180deg, #4b8ed8 0%, #2f6fc4 55%, #1f4f96 100%);
    opacity: 0.9;
  }

  .contact { position: absolute; left: 466px; top: 34px; right: 0; }
  .person-name {
    font-size: 41px;
    color: var(--teal-text);
    font-weight: 400;
    line-height: 1.2;
  }
  .person-name strong { font-weight: 700; }
  .contact-line {
    display: flex; align-items: center; gap: 18px;
    margin-top: 8px;
    font-size: 27px; color: var(--ink);
  }
  .contact-line svg { width: 28px; height: 28px; flex: none; }
  .phone { font-weight: 700; margin-top: 12px; }
  .email { font-size: 22px; font-weight: 500; }
  .rule { height: 2px; background: var(--teal-text); margin-top: 18px; }

  .services { list-style: none; margin-top: 18px; }
  .services li {
    display: flex; align-items: center; gap: 14px;
    font-size: 23px; color: var(--ink-soft);
    height: 34.3px;
  }
  .services svg { width: 23px; height: 23px; flex: none; }
</style>
</head>
<body>

<section class="card card-front">
  <svg class="card-bg" viewBox="0 0 960 548" aria-hidden="true">
    <defs>
      <radialGradient id="frontGlow" cx="480" cy="200" r="420" gradientUnits="userSpaceOnUse">
        <stop offset="0" stop-color="#52dcaa"/>
        <stop offset="0.55" stop-color="#2f9e80"/>
        <stop offset="1" stop-color="#1f8068"/>
      </radialGradient>
    </defs>
    <rect width="960" height="548" fill="url(#frontGlow)"/>
    <path d="M0,427 Q100,455 170,468 L790,468 Q860,455 960,427 V548 H0 Z" fill="#f9a825"/>
    <path d="M0,513 Q480,367 960,513 V548 H0 Z" fill="#ffffff"/>

    <g class="service-icons">
      <circle cx="241" cy="448" r="43" fill="#8ee21f"/>
      <g fill="none" stroke="#fff" stroke-width="4" stroke-linecap="round">
        <path d="M218,436 H250 a8,8 0 1 0 -8,-8"/>
        <path d="M214,448 H258 a9,9 0 1 1 -9,9"/>
        <path d="M222,460 H240"/>
      </g>

      <circle cx="401" cy="448" r="43" fill="#7ff0d7"/>
      <g stroke="#fff" stroke-width="4" stroke-linecap="round">
        <path d="M401,424 V472 M380,436 L422,460 M380,460 L422,436"/>
        <path d="M395,428 L401,434 L407,428 M395,468 L401,462 L407,468"/>
      </g>

      <circle cx="561" cy="448" r="43" fill="#0c1f6e"/>
      <path d="M561,422 C552,438 545,448 545,458 a16,16 0 0 0 32,0 C577,448 570,438 561,422 Z" fill="#fff"/>

      <circle cx="720" cy="448" r="43" fill="#f2511b"/>
      <path d="M720,420 C732,436 742,446 740,460 a20,20 0 0 1 -40,0 C700,448 708,442 712,432 C714,440 716,444 720,446 C722,438 722,430 720,420 Z" fill="#fff"/>
    </g>
  </svg>

  <div class="brand">
    <span class="brand-name">BELLCREST</span>
    <span class="brand-trade">HVAC</span>
  </div>
</section>

<section class="card card-back">
  <svg class="card-bg" viewBox="0 0 960 548" aria-hidden="true">
    <defs>
      <radialGradient id="backGlow" cx="60" cy="260" r="380" gradientUnits="userSpaceOnUse">
        <stop offset="0" stop-color="#52dcaa"/>
        <stop offset="1" stop-color="#1f8068"/>
      </radialGradient>
    </defs>
    <rect width="960" height="548" fill="#ffffff"/>
    <path d="M190,0 H395 C330,30 300,90 300,130 L300,548 H190 Z" fill="#f9a825"/>
    <path d="M0,0 H290 C370,40 370,140 370,270 C370,400 350,500 300,548 H0 Z" fill="url(#backGlow)"/>
    <path d="M330,548 C345,530 360,515 395,548 Z" fill="#f9a825"/>
  </svg>

  <div class="illustration-slot" role="img" aria-label="Cartoon HVAC technician in blue cap and overalls giving a thumbs up"></div>

  <div class="contact">
    <h1 class="person-name"><strong>Dorian</strong> Vance</h1>

    <p class="contact-line phone">
      <svg viewBox="0 0 24 24" aria-hidden="true"><path d="M6.6 10.8a15 15 0 0 0 6.6 6.6l2.2-2.2a1 1 0 0 1 1-.25 11 11 0 0 0 3.6.57 1 1 0 0 1 1 1V20a1 1 0 0 1-1 1A17 17 0 0 1 3 4a1 1 0 0 1 1-1h3.5a1 1 0 0 1 1 1 11 11 0 0 0 .57 3.6 1 1 0 0 1-.25 1Z" fill="#1e7d66"/></svg>
      555-318-4702
    </p>

    <p class="contact-line email">
      <svg viewBox="0 0 24 24" aria-hidden="true"><rect x="2" y="5" width="20" height="14" rx="1.5" fill="#1e7d66"/><path d="M3 6.5 12 13l9-6.5" fill="none" stroke="#fff" stroke-width="1.6"/></svg>
      dvance@bellcresthvac-example.net
    </p>

    <div class="rule"></div>

    <ul class="services">
      <li><svg viewBox="0 0 24 24" aria-hidden="true"><circle cx="12" cy="12" r="12" fill="#1e7d66"/><path d="M6.5 12.5l3.8 3.6 7.2-7.6" fill="none" stroke="#fff" stroke-width="2.8" stroke-linecap="round" stroke-linejoin="round"/></svg>Air Conditioning</li>
      <li><svg viewBox="0 0 24 24" aria-hidden="true"><circle cx="12" cy="12" r="12" fill="#1e7d66"/><path d="M6.5 12.5l3.8 3.6 7.2-7.6" fill="none" stroke="#fff" stroke-width="2.8" stroke-linecap="round" stroke-linejoin="round"/></svg>Heating</li>
      <li><svg viewBox="0 0 24 24" aria-hidden="true"><circle cx="12" cy="12" r="12" fill="#1e7d66"/><path d="M6.5 12.5l3.8 3.6 7.2-7.6" fill="none" stroke="#fff" stroke-width="2.8" stroke-linecap="round" stroke-linejoin="round"/></svg>Heat Pump / Gas / Oil</li>
      <li><svg viewBox="0 0 24 24" aria-hidden="true"><circle cx="12" cy="12" r="12" fill="#1e7d66"/><path d="M6.5 12.5l3.8 3.6 7.2-7.6" fill="none" stroke="#fff" stroke-width="2.8" stroke-linecap="round" stroke-linejoin="round"/></svg>Controls</li>
      <li><svg viewBox="0 0 24 24" aria-hidden="true"><circle cx="12" cy="12" r="12" fill="#1e7d66"/><path d="M6.5 12.5l3.8 3.6 7.2-7.6" fill="none" stroke="#fff" stroke-width="2.8" stroke-linecap="round" stroke-linejoin="round"/></svg>VFD's</li>
      <li><svg viewBox="0 0 24 24" aria-hidden="true"><circle cx="12" cy="12" r="12" fill="#1e7d66"/><path d="M6.5 12.5l3.8 3.6 7.2-7.6" fill="none" stroke="#fff" stroke-width="2.8" stroke-linecap="round" stroke-linejoin="round"/></svg>Pumps</li>
      <li><svg viewBox="0 0 24 24" aria-hidden="true"><circle cx="12" cy="12" r="12" fill="#1e7d66"/><path d="M6.5 12.5l3.8 3.6 7.2-7.6" fill="none" stroke="#fff" stroke-width="2.8" stroke-linecap="round" stroke-linejoin="round"/></svg>Gas Fitting / Piping</li>
      <li><svg viewBox="0 0 24 24" aria-hidden="true"><circle cx="12" cy="12" r="12" fill="#1e7d66"/><path d="M6.5 12.5l3.8 3.6 7.2-7.6" fill="none" stroke="#fff" stroke-width="2.8" stroke-linecap="round" stroke-linejoin="round"/></svg>Service and New install</li>
      <li><svg viewBox="0 0 24 24" aria-hidden="true"><circle cx="12" cy="12" r="12" fill="#1e7d66"/><path d="M6.5 12.5l3.8 3.6 7.2-7.6" fill="none" stroke="#fff" stroke-width="2.8" stroke-linecap="round" stroke-linejoin="round"/></svg>Residential / Commercial</li>
    </ul>
  </div>
</section>

</body>
</html>
```